Health and Wellness Company Business Card

I need a business card design that is clean and uses modern minimalist style. The design should incorporate our logo (see attached). I would also like to use embossing on the cards so that they also have a great feel. I am open to the card using one or more colors, and these do not have to correspond to the colors in the concept paper. The card can either be one-sided or use both sides of the card.The logo uses the Avenir font.

I will need the file designed in Adobe CS and compatible with CS5.5 (Illustrator preferable) and I'll need the working file (for example: .ai) once the project is complete so that I can change the names/contact info/etc for each variation of the card.

This needs to be a memorable card for the recipient. They should think: "This is a great business card" either because of its simplicity or embossing effects or use of color.

Target Market(s)

The audience for our company has two main groups: people who pay for healthcare (insurers, companies, researcher companies) and people with chronic health conditions who are the consumers of our services and resources.

Industry/Entity Type

Business

Requirements
Must have
• Essential components of the card include: Company logo, contact Name (Mark Dalton), phone number (5049381726), email address (mdalton@brevolin.com), slogan/tagline that consists of ~30-40 characters (Use Lorem Ipsum)
Nice to have
• These fall just slightly short of "must have" to allow for design flexibility: Embossing or spot varnish effects and a splash of color
Should not have
• Designs with these components will not be successful: flashy or showy designs that are not professional in appearance, and lots of different colors

```html
<!DOCTYPE html>
<html lang="en">
<head>
<meta charset="utf-8">
<title>Brevolin Business Card</title>
<link rel="stylesheet" href="https://fonts.googleapis.com/css2?family=Nunito+Sans:wght@400;600;700&display=swap">
<style>
  :root {
    --bg: #efeff0;
    --card-white: #ffffff;
    --lavender-dark: #767897;
    --lavender-light: #aeb0c6;
    --logo-grey: #9a9aa4;
    --name-purple: #8a7591;
    --contact-purple: #7a6780;
    --shadow: rgba(60, 60, 80, 0.18);
  }
  * { margin: 0; padding: 0; box-sizing: border-box; }
  html, body {
    width: 1200px; height: 864px; overflow: hidden;
    background: var(--bg);
    font-family: "Nunito Sans", "Avenir", sans-serif;
  }
  .canvas { position: relative; width: 1200px; height: 864px; }
  .card {
    position: absolute;
    width: 560px; height: 320px;
    border-radius: 28px;
    box-shadow: 0 10px 28px var(--shadow);
  }
  .card-back {
    left: 90px; top: 80px;
    background: linear-gradient(90deg, var(--lavender-dark) 0%, var(--lavender-dark) 30%, var(--lavender-light) 100%);
    display: flex; align-items: center; justify-content: center;
  }
  .back-brand {
    display: flex; align-items: center; gap: 18px;
    color: var(--card-white);
    font-size: 34px; font-weight: 600; letter-spacing: 0.32em;
  }
  .brand-mark {
    width: 30px; height: 30px; border-radius: 50%;
    background: currentColor;
  }
  .card-front {
    left: 550px; top: 464px;
    background: var(--card-white);
  }
  .front-brand {
    position: absolute; left: 0; right: 0; top: 96px;
    display: flex; flex-direction: column; align-items: center; gap: 14px;
    color: var(--logo-grey);
    font-size: 28px; font-weight: 600; letter-spacing: 0.34em;
  }
  .front-brand .brand-mark { width: 40px; height: 40px; }
  .contact {
    position: absolute; right: 34px; top: 34px;
    list-style: none;
    color: var(--contact-purple);
    font-size: 15px; line-height: 22px; text-align: right;
  }
  .contact li { display: flex; justify-content: flex-end; align-items: center; gap: 7px; }
  .contact svg { width: 13px; height: 13px; fill: var(--contact-purple); }
  .person {
    position: absolute; left: 40px; bottom: 38px;
    color: var(--name-purple);
  }
  .person-name { font-size: 20px; font-weight: 700; letter-spacing: 0.02em; }
  .person-role { font-size: 16px; font-weight: 400; margin-top: -2px; }
</style>
</head>
<body>
<main class="canvas">
  <section class="card card-back">
    <div class="back-brand"><span class="brand-mark"></span><span>BREVOLIN</span></div>
  </section>

  <section class="card card-front">
    <div class="front-brand"><span class="brand-mark"></span><span>BREVOLIN</span></div>

    <ul class="contact">
      <li>5049381726
        <svg viewBox="0 0 16 16" aria-hidden="true"><path d="M3.6 1.5l2.3 2.6-1.3 1.7c.9 2 2.6 3.7 4.6 4.6l1.7-1.3 2.6 2.3-1.2 2c-5.6-.3-10.4-5.1-10.7-10.7z"/></svg>
      </li>
      <li>mdalton@brevolin.com
        <svg viewBox="0 0 16 16" aria-hidden="true"><path d="M1 3h14v10H1zM2 4.3v.4l6 4 6-4v-.4z"/></svg>
      </li>
      <li>www.brevolin.com
        <svg viewBox="0 0 16 16" aria-hidden="true"><circle cx="8" cy="8" r="6.5" fill="none" stroke="#7a6780" stroke-width="1.3"/><path d="M1.5 8h13M8 1.5c-3 3.5-3 9.5 0 13M8 1.5c3 3.5 3 9.5 0 13" fill="none" stroke="#7a6780" stroke-width="1.1"/></svg>
      </li>
    </ul>

    <div class="person">
      <p class="person-name">MARK DALTON</p>
      <p class="person-role">President</p>
    </div>
  </section>
</main>
</body>
</html>
```